Design the app for the next NestLoop

We need a cutting edge, super UX-intuitive, design for a global parking app called Vamo.
- Homescreen and website have been finalised already (see attached pdf)
- Wireframed screens for the concepts we need have been provided in the attached pdf
- We need some really nice icons for parking space types, etc
- Needs to be very, very intuitive to use and navigate.
References: NestLoop app & Zolt app, for their simplicity of use
Updates
Project Deadline Extended
Reason: A few designers have requested that we extend this deadline. So here you go.
Industry/Entity Type
Parking
Look and feel
Each slider illustrates characteristics of the customer's brand and the style your logo design should communicate.

```html
<!DOCTYPE html>
<html lang="en">
<head>
<meta charset="utf-8">
<title>Vamo – App Screens</title>
<link href="https://fonts.googleapis.com/css2?family=Roboto:wght@400;500;700&display=swap" rel="stylesheet">
<style>
  :root{
    --bg:#4dbf8a;
    --ink:#111;
    --muted:#8a8a8a;
    --line:#dcdcdc;
    --panel:#f2f2f2;
    --white:#fff;
    --dark:#0d0d0d;
  }
  *{box-sizing:border-box;margin:0;padding:0}
  html,body{width:1200px;height:1020px;overflow:hidden}
  body{background:var(--bg);font-family:"Roboto",Arial,sans-serif;color:var(--ink);position:relative}
  .screen{position:absolute;top:80px;width:150px;background:var(--white);overflow:hidden}
  .screen > *{position:absolute}
  .status{left:0;top:0;width:150px;height:9px;background:var(--dark);color:#fff;font-size:4px;display:flex;justify-content:space-between;align-items:center;padding:0 5px}
  .status .batt{display:inline-block;width:8px;height:3px;background:#fff;margin-left:2px;vertical-align:middle}
  .topbar{left:0;top:9px;width:150px;height:21px;border-bottom:1px solid var(--line);display:flex;align-items:center;justify-content:center;font-size:5.5px;font-weight:500;background:#fff}
  .topbar .back{position:absolute;left:7px;top:4px;font-size:10px;font-weight:400}
  .topbar .action{position:absolute;right:4px;top:5px;border:1px solid var(--line);font-size:4.5px;padding:2px 4px;font-weight:400}
  .label{font-size:4.3px;color:var(--muted);left:6px}
  .field{left:6px;width:138px;border:1px solid var(--line);background:#fff}
  .btn{border:1px solid var(--line);background:#fff;font-size:4.5px;display:flex;align-items:center;justify-content:center}
  .tabbar{left:0;top:246px;width:150px;height:20px;border-top:1px solid var(--line);background:#fff;display:flex}
  .tab{flex:1;display:flex;flex-direction:column;align-items:center;justify-content:center;font-size:3.6px;color:var(--muted);gap:1px}
  .tab.active{color:var(--ink);font-weight:500}
  .tab svg{display:block}
  .map{background:linear-gradient(120deg,#e9e9e9 0%,#e0e0e0 40%,#d6d6d6 62%,#c7c7c7 78%,#d2d2d2 100%)}
  .compass{width:11px;height:11px;border-radius:50%;background:#2a2a2a}
  .dot{width:7px;height:7px;border-radius:50%;background:#9a9a9a;border:1.5px solid #fff;box-shadow:0 0 0 1px #888}
  .days{display:flex}
  .days span{flex:1;display:flex;align-items:center;justify-content:center;font-weight:500}
  .days span.on{background:var(--dark);color:#fff}

  /* screen 1 */
  .splash{left:82px;height:266px;background:var(--dark)}
  .splash .photo{left:0;top:0;width:150px;height:266px;background:linear-gradient(170deg,#2b2e31 0%,#1e2124 35%,#16191c 60%,#0c0d0e 100%)}
  .splash .login{right:6px;top:12px;background:#fff;font-size:4.5px;padding:3px 5px}
  .brand{left:0;top:96px;width:150px;display:flex;flex-direction:column;align-items:center;gap:8px;color:#fff}
  .brand .mark{width:38px;height:38px;background:#fff;border-radius:3px}
  .brand .name{font-size:9px;letter-spacing:4px;font-weight:400}
  .splash .btn{left:6px;width:138px;height:17px;border:0}

  /* screen 2 */
  .how{left:253px;height:352px;background:var(--dark)}
  .how .card{left:6px;top:32px;width:138px;height:302px;background:#fff}
  .how .card > *{position:absolute}
  .how h2{top:6px;width:138px;text-align:center;font-size:7px;font-weight:500}
  .how .art{left:49px;width:42px;height:42px;border-radius:50%;border:1px solid #e4e4e4}
  .art.locate{background:radial-gradient(circle at 50% 60%,#6fa8c9 0%,#a9cbe0 35%,#eef2f4 70%)}
  .art.phone{background:radial-gradient(circle at 50% 55%,#e9a27a 0%,#5f9fcf 40%,#8cc0e2 70%)}
  .art.park{background:radial-gradient(circle at 50% 55%,#d9453c 0%,#e57a6a 30%,#a8d3b8 55%,#f0f3f2 75%)}
  .how .step{left:6px;width:128px;font-size:3.8px;line-height:1.4;color:#444}
  .how .step b{display:block;font-size:5px;color:var(--ink);font-weight:700}
  .how .card .btn{left:49px;top:278px;width:54px;height:14px}

  /* screen 3 */
  .find{left:424px;height:266px}
  .pop{left:36px;top:36px;width:108px;height:54px;background:#fff;box-shadow:0 1px 3px rgba(0,0,0,.25);font-size:4px}
  .pop > *{position:absolute}
  .pin{width:12px;height:12px;border-radius:50%;background:#111;border:2px solid #fff;box-shadow:0 0 0 1px #111}
  .pin:after{content:"";position:absolute;left:3px;top:11px;width:2px;height:8px;background:#111}

  /* screen 4 */
  .detail{left:595px;height:884px}
  .cal{left:6px;top:526px;width:138px;height:40px;background:var(--dark);color:#fff}
  .grid{left:6px;top:570px;width:138px;display:grid;grid-template-columns:repeat(7,1fr);row-gap:9.5px;font-size:7px;color:#555;text-align:center}
  .grid .dim{color:#c9c9c9}
  .grid .sel{background:#111;color:#fff;border-radius:50%;width:15px;height:15px;line-height:15px;margin:-3px auto 0}
  .chip{height:16px;border:1px solid var(--line);font-size:4px;color:var(--muted);display:flex;align-items:center;gap:8px;padding-left:5px;width:66px}
  .feat{flex:1;display:flex;flex-direction:column;align-items:center;justify-content:center;gap:1px;font-size:3.6px;color:#555}

  /* screen 5 */
  .add{left:766px;height:266px;background:var(--panel)}
  .menu{left:0;width:150px;height:18px;background:#fff;display:flex;align-items:center;font-size:5px;padding-left:6px;gap:7px;border-bottom:1px solid var(--line)}
  .menu.on{background:var(--dark);color:#fff}
  .menu em{font-style:normal;width:8px;height:8px;border-radius:50%;display:flex;align-items:center;justify-content:center;font-size:4px;background:#eee;color:#111}
  .menu.on em{background:#fff}
  .menu:after{content:"›";position:absolute;right:7px;font-size:9px}

  /* screen 6 */
  .describe{left:938px;height:474px}
  .field.tall{height:18px}
</style>
</head>
<body>

<!-- 1 Splash -->
<section class="screen splash">
  <div class="photo" role="img" aria-label="Dark photo of a parked scooter"></div>
  <div class="status"><span>●●●●● NOVA</span><span>4:21 PM</span><span>22%<i class="batt"></i></span></div>
  <div class="login">Login</div>
  <div class="brand"><div class="mark"></div><div class="name">VAMO</div></div>
  <div class="btn" style="top:223px">Lease your parking space</div>
  <div class="btn" style="top:243px">⌕ Search for parking</div>
</section>

<!-- 2 How it works -->
<section class="screen how">
  <div class="status"><span>●●●●● NOVA</span><span>4:21 PM</span><span>22%<i class="batt"></i></span></div>
  <div class="card">
    <h2>How It Works</h2>
    <div class="art locate" style="top:24px" role="img" aria-label="Illustration of a car with a map pin"></div>
    <p class="step" style="top:78px"><b>Locate An Affordable Parking Space Near You</b>Find Someone Who Has An Empty Space Near You Can Park Your Car, Motorbike, Boat Or Helicopter. This Might Be An Empty Driveway, A Garage, A Mooring Or Even A Building Rooftop.</p>
    <div class="art phone" style="top:118px" role="img" aria-label="Illustration of a hand holding a phone"></div>
    <p class="step" style="top:172px"><b>Select Your Booking Time And Dates</b>Check Availability, Confirm The Cost, Then Pay Through</p>
    <div class="art park" style="top:196px" role="img" aria-label="Illustration of a parked car"></div>
    <p class="step" style="top:250px"><b>Park Your Vehicle</b>Save Time, Spend Less. Sleep Easy. Your Vehicle Now Has Its Own Private Parking Space.</p>
    <div class="btn">Start Parking Now</div>
  </div>
</section>

<!-- 3 Find a space -->
<section class="screen find">
  <div class="status"><span>●●●●● NOVA</span><span>4:21 PM</span><span>22%<i class="batt"></i></span></div>
  <div class="topbar">Vamo
    <svg style="position:absolute;left:6px;top:6px" width="9" height="9"><circle cx="4.5" cy="4.5" r="4" fill="none" stroke="#999" stroke-width=".7"/><path d="M4.5 4v3M4.5 2.3v.6" stroke="#999" stroke-width=".7"/></svg>
    <svg style="position:absolute;right:6px;top:6px" width="9" height="9"><path d="M0.5 0.5h8L5 4.5v4L4 7.5V4.5z" fill="none" stroke="#999" stroke-width=".7"/></svg>
  </div>
  <div class="map" style="left:0;top:30px;width:150px;height:216px" role="img" aria-label="City street map with parking spots"></div>
  <div class="pop">
    <div style="left:6px;top:6px;width:11px;height:11px;border-radius:50%;background:#bbb"></div>
    <div style="left:4px;top:16px;width:15px;height:10px;border-radius:7px 7px 0 0;background:#bbb"></div>
    <div style="left:17px;top:15px;font-size:3.5px">+10</div>
    <svg style="left:30px;top:4px" width="26" height="10"><path d="M1 8V5.5l2.5-3h7l2.5 3V8z" fill="#111"/><circle cx="3.5" cy="8.5" r="1.2" fill="#111"/><circle cx="10.5" cy="8.5" r="1.2" fill="#111"/><rect x="18" y="4.5" width="6" height="5" fill="#111"/><path d="M19.2 4.5V3a1.8 1.8 0 0 1 3.6 0v1.5" fill="none" stroke="#111" stroke-width=".9"/></svg>
    <div style="left:62px;top:6px">Price <b>$10 day</b></div>
    <div style="left:48px;top:21px">Available <b>7am - 6pm</b></div>
    <div style="right:4px;top:14px;font-size:9px">›</div>
    <div class="days" style="left:4px;top:41px;width:100px;height:10px;font-size:4px"><span class="on">S</span><span>M</span><span>T</span><span>W</span><span>T</span><span>F</span><span>S</span></div>
  </div>
  <div class="pin" style="left:113px;top:128px"></div>
  <div class="pin" style="left:113px;top:172px"></div>
  <div class="pin" style="left:67px;top:186px"></div>
  <nav class="tabbar">
    <div class="tab active"><svg width="8" height="6"><path d="M.5 5V3.5L2 1.5h4l1.5 2V5z" fill="#111"/></svg>Find a Space</div>
    <div class="tab"><svg width="7" height="7"><rect x=".5" y="1" width="6" height="5.5" fill="none" stroke="#999" stroke-width=".7"/></svg>Booking</div>
    <div class="tab"><svg width="7" height="7"><rect x=".5" y=".5" width="6" height="6" fill="none" stroke="#999" stroke-width=".7"/><path d="M.5 3h6" stroke="#999" stroke-width=".7"/></svg>Your Spaces</div>
    <div class="tab"><svg width="7" height="7"><circle cx="3.5" cy="2" r="1.6" fill="#999"/><path d="M.5 7a3 3 0 0 1 6 0z" fill="#999"/></svg>Profile</div>
  </nav>
</section>

<!-- 4 Parking space detail -->
<section class="screen detail">
  <div class="status"><span>●●●●● NOVA</span><span>4:21 PM</span><span>22%<i class="batt"></i></span></div>
  <div class="topbar"><span class="back">‹</span>Parking Space<span class="action" style="border:0;border-left:1px solid var(--line)">Book Now</span></div>
  <div class="map" style="left:0;top:30px;width:150px;height:71px" role="img" aria-label="Map around the parking space"></div>
  <div class="compass" style="left:134px;top:33px"></div>
  <div class="dot" style="left:81px;top:67px"></div>
  <div style="left:42px;top:115px;width:26px;height:26px;border-radius:50%;background:radial-gradient(circle at 50% 40%,#d8d8d8,#9a9a9a)" role="img" aria-label="Owner portrait"></div>
  <div style="left:77px;top:124px;font-size:7px;font-weight:700">Lewis Marden</div>
  <div class="field" style="top:155px;height:16px;font-size:4.3px;display:flex;align-items:center;gap:6px;padding-left:4px">
    <svg width="18" height="7"><path d="M1 6V4l3-3h9l3 3v2z" fill="none" stroke="#555" stroke-width=".8"/></svg>Safe parking spot 10min walk for ......</div>
  <div style="left:0;top:179px;width:150px;height:71px;background:linear-gradient(175deg,#a7adb4 0%,#6e747b 35%,#3a3e43 60%,#c86a2c 78%,#2d3033 100%)" role="img" aria-label="Photo of a sports car on a road"></div>
  <div style="left:62px;top:243px;display:flex;gap:3px"><i style="width:5px;height:5px;border:1px solid #fff;border-radius:50%"></i><i style="width:5px;height:5px;background:#fff;border-radius:50%"></i><i style="width:5px;height:5px;border:1px solid #fff;border-radius:50%"></i></div>

  <div class="label" style="top:259px">Ideal for</div><div class="field" style="top:265px;height:17px"></div>
  <div class="label" style="top:290px">Description</div><div class="field" style="top:296px;height:52px"></div>
  <div class="label" style="top:356px">Features</div>
  <div class="field" style="top:362px;height:17px;display:flex">
    <span class="feat"><svg width="6" height="6"><rect x=".5" y="2.5" width="5" height="3.5" fill="#111"/><path d="M1.5 2.5V1.8a1.5 1.5 0 0 1 3 0v.7" fill="none" stroke="#111" stroke-width=".8"/></svg>Secure</span>
    <span class="feat"><svg width="7" height="6"><path d="M.5 2L3.5.5 6.5 2v3.5h-6z" fill="none" stroke="#666" stroke-width=".7"/></svg>Covered</span>
    <span class="feat"><svg width="6" height="6"><circle cx="3" cy="2" r="1.5" fill="#888"/><path d="M.5 6a2.5 2.5 0 0 1 5 0z" fill="#888"/></svg>Guarded</span>
    <span class="feat"><svg width="8" height="6"><path d="M.5 5V1.5h5v1.5h1.5L7.5 4v1z" fill="#888"/></svg>Large</span>
  </div>
  <div class="label" style="top:387px">Address</div><div class="field" style="top:392px;height:36px"></div>
  <div class="label" style="top:436px">Price</div><div class="field" style="top:442px;height:17px;width:66px"></div>
  <div class="label" style="top:467px">Availability</div>
  <div class="field btn" style="top:472px;height:17px;font-size:4.3px">8am - 7pm</div>
  <div class="days" style="left:6px;top:494px;width:138px;height:19px;font-size:7px"><span class="on">S</span><span>M</span><span>T</span><span>W</span><span>T</span><span>F</span><span>S</span></div>
  <div class="label" style="top:521px">Select Days</div>
  <div class="cal">
    <div style="display:flex;justify-content:space-between;padding:5px 8px 0;font-size:9px"><span>‹</span><span style="font-size:8px">September</span><span>›</span></div>
    <div style="display:grid;grid-template-columns:repeat(7,1fr);text-align:center;font-size:6.5px;margin-top:7px"><span>S</span><span>M</span><span>T</span><span>W</span><span>T</span><span>F</span><span>S</span></div>
  </div>
  <div class="grid">
    <span class="dim">24</span><span class="dim">25</span><span class="dim">26</span><span class="dim">27</span><span class="dim">28</span><span>1</span><span>2</span>
    <span>3</span><span>4</span><span><div class="sel">5</div></span><span>6</span><span>7</span><span>8</span><span>9</span>
    <span>10</span><span>11</span><span>12</span><span>13</span><span>14</span><span>15</span><span>16</span>
    <span>17</span><span>18</span><span>19</span><span>20</span><span>21</span><span>22</span><span>23</span>
    <span>24</span><span>25</span><span>26</span><span>27</span><span>28</span><span class="dim">1</span><span class="dim">2</span>
  </div>
  <div class="field btn" style="top:674px;height:17px">Book all available days this month</div>
  <div class="label" style="top:699px">Days Select</div>
  <div class="chip" style="left:6px;top:706px;color:#333"><span>Sunday</span><span>9 April 2016</span></div>
  <div class="chip" style="left:78px;top:706px"><span>Monday</span><span>25 April 2016</span></div>
  <div class="chip" style="left:6px;top:727px"><span>Thursday</span><span>11 April 2016</span></div>
  <div class="chip" style="left:6px;top:748px"><span>Monday</span><span>18 April 2016</span></div>
  <div class="chip" style="left:6px;top:769px"><span>Friday</span><span>22 April 2016</span></div>
  <div style="left:42px;top:792px;width:66px;height:17px;background:var(--dark);color:#fff;font-size:6.5px;display:flex;align-items:center;justify-content:center">Total $60</div>
  <div class="label" style="top:816px">Message to Owner</div><div class="field" style="top:822px;height:34px"></div>
  <div class="field btn" style="top:862px;height:14px">Request Now</div>
</section>

<!-- 5 Add your space -->
<section class="screen add">
  <div class="status"><span>●●●●● NOVA</span><span>4:21 PM</span><span>22%<i class="batt"></i></span></div>
  <div class="topbar"><span class="back">‹</span>Add your space<span class="action">Preview</span></div>
  <div class="menu on" style="top:34px"><em>1</em>Describe your space</div>
  <div class="menu" style="top:55px"><em>2</em>Select Features</div>
  <div class="menu" style="top:76px"><em>3</em>Add Photo</div>
  <div class="menu" style="top:97px"><em>4</em>Choose Availability</div>
  <div class="menu" style="top:118px"><em>5</em>Set Price</div>
  <div class="btn" style="left:6px;top:231px;width:138px;height:13px">Preview your space</div>
  <nav class="tabbar">
    <div class="tab active"><svg width="8" height="6"><path d="M.5 5V3.5L2 1.5h4l1.5 2V5z" fill="#111"/></svg>Find a Space</div>
    <div class="tab"><svg width="7" height="7"><rect x=".5" y="1" width="6" height="5.5" fill="none" stroke="#999" stroke-width=".7"/></svg>Booking</div>
    <div class="tab"><svg width="7" height="7"><rect x=".5" y=".5" width="6" height="6" fill="none" stroke="#999" stroke-width=".7"/><path d="M.5 3h6" stroke="#999" stroke-width=".7"/></svg>Your Spaces</div>
    <div class="tab"><svg width="7" height="7"><circle cx="3.5" cy="2" r="1.6" fill="#999"/><path d="M.5 7a3 3 0 0 1 6 0z" fill="#999"/></svg>Profile</div>
  </nav>
</section>

<!-- 6 Describe -->
<section class="screen describe">
  <div class="status"><span>●●●●● NOVA</span><span>4:21 PM</span><span>22%<i class="batt"></i></span></div>
  <div class="topbar"><span class="back">‹</span>Describe</div>
  <div style="left:67px;top:41px;width:16px;height:16px;border-radius:50%;background:#eee;font-size:6px;display:flex;align-items:center;justify-content:center">1</div>
  <div class="label" style="top:62px">Type</div>
  <svg style="left:6px;top:70px" width="104" height="14">
    <rect x="0" y="0" width="104" height="14" fill="none" stroke="#ddd" stroke-width=".6"/>
    <path d="M4 10V7l4-3h9l4 3v3z" fill="#111"/><circle cx="8" cy="10.5" r="1.5" fill="#111"/><circle cx="17" cy="10.5" r="1.5" fill="#111"/>
    <g fill="none" stroke="#999" stroke-width=".8"><circle cx="32" cy="9" r="2.5"/><circle cx="41" cy="9" r="2.5"/><path d="M32 9l4-4h5"/>
    <path d="M56 10h12l-2 2h-8z"/><path d="M62 3v7M62 3l4 6"/>
    <path d="M80 7h10a2 2 0 0 1 0 4h-8z M78 5h16M86 5v2"/></g>
  </svg>
  <div class="label" style="top:93px">Title</div><div class="field" style="top:98px;height:18px"></div>
  <div class="label" style="top:125px">Description</div><div class="field" style="top:130px;height:52px"></div>
  <div class="label" style="top:190px">Ideal for</div><div class="field tall" style="top:195px"></div>
  <div class="label" style="top:222px">Instruction</div><div class="field tall" style="top:226px"></div>
  <div class="label" style="top:252px">Suburb</div><div class="field tall" style="top:258px"></div>
  <div class="label" style="top:284px">State</div><div class="field tall" style="top:289px"></div>
  <div class="label" style="top:314px">Postal Code</div><div class="field tall" style="top:319px"></div>
  <div class="label" style="top:345px">Country</div>
  <div class="field" style="top:350px;height:19px;font-size:5px;display:flex;align-items:center;gap:5px;padding-left:6px">
    <i style="width:8px;height:6px;background:#24397a"></i>Australia<span style="position:absolute;right:6px;font-size:6px">⌄</span></div>
  <div class="map" style="left:0;top:374px;width:150px;height:73px" role="img" aria-label="Map to pin the space location"></div>
  <div class="compass" style="left:134px;top:377px"></div>
  <div class="dot" style="left:82px;top:414px"></div>
  <div class="btn" style="left:6px;top:453px;width:138px;height:13px">Next Step</div>
</section>

</body>
</html>
```